Web Design for Recruitment Agency

We need a new web design for the company who provides professional services in Labor Recruitment and Home Helpers Hire.

The sections to be covered:
1. About us
2. Philosophy
3. Services
- Labor Recruitment
* skilled workers
* unskilled workers
- Home Helpers
4. Search CV
5. Testimonials
5. Contact us

Examples:
http://www.qorvennaue.com
http://tpmubelo.ae

The website should be clean and elegant. It should portray professionalism and attention to details.

It is important to have interactive and easy-to-navigate design with lots of pictures.

We want clients to get the right impression and be able to request a contact in case they have a requirement. We also want clients to be able to search for CVs that are already in the database. CV should be displayed as a profile card (photo and brief information about the candidate).

Logo is attached.

Target Market(s)

Local families, companies.

Industry/Entity Type

It Company

Number of Pages Required

1 page

Font styles to use
Sans Serif

Requirements
Must have
• Clean layout with pictures
Nice to have
• Dynamic, engaging website.

```html
<!DOCTYPE html>
<html lang="en">
<head>
<meta charset="utf-8">
<title>KTV Recruitment</title>
<link href="https://fonts.googleapis.com/css2?family=Montserrat:wght@400;700&family=Open+Sans:wght@400;600&display=swap" rel="stylesheet">
<style>
:root{
  --green:#2aa33c;
  --green-dark:#1f8a2e;
  --green-text:#1e7f2c;
  --purple:#6a3fd0;
  --ink:#2a2a2a;
  --muted:#8a8a8a;
  --soft:#f2f2f2;
  --line:#d8d8d8;
  --white:#ffffff;
}
*{box-sizing:border-box;margin:0;padding:0}
html,body{width:694px;height:1200px;overflow:hidden}
body{position:relative;background:var(--soft);font-family:"Open Sans",sans-serif;color:var(--muted);font-size:7px;line-height:1.7}
.abs{position:absolute}
h2,h3,h4,.nav a,.brand,.cta{font-family:"Montserrat",sans-serif}

.topbar{left:0;top:0;width:694px;height:70px;background:var(--soft)}
.brand{left:57px;top:16px;display:flex;align-items:center;gap:6px;font-weight:700;font-size:14px;color:var(--green-text)}
.brand i{width:12px;height:12px;border-radius:50%;background:var(--green);display:block}
.contact-item{display:flex;align-items:flex-start;gap:8px;font-size:7.5px;color:var(--muted);line-height:1.4}
.social{left:578px;top:28px;display:flex;gap:8px}
.social span{width:13px;height:13px;background:#333;display:block;border-radius:2px}

.nav{left:0;top:70px;width:694px;height:34px;background:linear-gradient(#35b547,var(--green-dark))}
.nav ul{list-style:none;display:flex;margin-left:60px;height:100%}
.nav a{display:flex;align-items:center;height:34px;padding:0 13.5px;color:var(--white);font-size:8.5px;text-decoration:none;border-right:1px solid rgba(255,255,255,.25)}
.nav li:last-child a{border-right:0}
.nav a.active{background:var(--purple);padding:0 13px 0 27px}

.hero{left:0;top:104px;width:694px;height:283px;background:linear-gradient(90deg,#d9d9d9,#6a5a50 25%,#e0dcd8 45%,#5d5350 70%,#ececec)}
.hero-box{left:216px;top:80px;width:262px;height:146px;background:rgba(40,40,40,.8);padding:14px 16px;color:var(--white)}
.hero-box h2{font-size:19px;line-height:1.3;font-weight:700}
.hero-box p{font-size:6.5px;color:#ddd;margin:8px 0 14px;line-height:1.8}
.btn{display:inline-block;background:var(--green);color:var(--white);font-family:"Montserrat",sans-serif;font-weight:700;font-size:8px;padding:8px 8px;border-radius:2px}
.arrow{width:26px;height:33px;background:rgba(110,110,110,.85);display:flex;align-items:center;justify-content:center;top:225px}

.cta{left:0;top:387px;width:694px;height:62px;background:linear-gradient(#35b547,var(--green-dark));display:flex;align-items:center;justify-content:center;gap:12px;color:var(--white);font-weight:700;font-size:13.5px}
.cta span.outline{border:1px solid var(--white);border-radius:2px;padding:6px 9px;font-size:14px}

.section-title{font-size:17px;font-weight:700;color:var(--ink);font-family:"Montserrat",sans-serif}
.rule{height:1px;background:var(--line)}
.rule b{display:block;height:3px;background:var(--green);position:relative;top:-1px}

.service{display:flex;gap:12px;width:290px}
.service .photo{width:94px;height:70px;flex:none}
.service h3{font-size:11.5px;color:var(--green-text);font-weight:400;margin:0 0 6px}
.service p{font-size:7px;line-height:1.75}

.white-band{left:0;top:742px;width:694px;height:245px;background:var(--white)}
.sq{width:26px;height:26px;border:1px solid #bbb;display:flex;align-items:center;justify-content:center}

.footer{left:0;top:987px;width:694px;height:172px;background:var(--soft)}
.footer h4{font-size:11.5px;font-weight:700;color:var(--ink);margin-bottom:12px}
.footer ul{list-style:none;font-size:6.8px;line-height:1.75}
.bottom{left:0;top:1159px;width:694px;height:41px;background:var(--green);color:var(--white);font-size:7.5px;display:flex;align-items:center;justify-content:center}
</style>
</head>
<body>

<header class="abs topbar">
  <div class="abs brand"><i></i>KTV</div>
  <div class="abs contact-item" style="left:303px;top:30px">
    <svg width="9" height="9" viewBox="0 0 24 24"><path fill="#999" d="M6.6 10.8a15 15 0 006.6 6.6l2.2-2.2a1 1 0 011-.25 11 11 0 003.6.6 1 1 0 011 1V20a1 1 0 01-1 1A17 17 0 013 4a1 1 0 011-1h3.5a1 1 0 011 1 11 11 0 00.6 3.6 1 1 0 01-.25 1z"/></svg>
    <span>+ 100 2 555 0199</span>
  </div>
  <div class="abs contact-item" style="left:408px;top:26px;width:150px">
    <svg width="8" height="8" viewBox="0 0 24 24"><path fill="#999" d="M12 3l10 9h-3v9h-5v-6h-4v6H5v-9H2z"/></svg>
    <span>Nemo enim ipsam voluptatem quia voluptas sit</span>
  </div>
  <div class="abs social"><span></span><span></span><span></span></div>
</header>

<nav class="abs nav">
  <ul>
    <li><a class="active" href="#">HOME</a></li>
    <li><a href="#">ABOUT US</a></li>
    <li><a href="#">PHILOSOPHY</a></li>
    <li><a href="#">SERVICES</a></li>
    <li><a href="#">SEARCH CV</a></li>
    <li><a href="#">TESTIMONIALS</a></li>
    <li><a href="#">CONTACT US</a></li>
  </ul>
</nav>

<section class="abs hero" role="img" aria-label="Smiling team of office professionals in business attire">
  <div class="abs hero-box" style="top:80px">
    <h2>Welcome to<br>KTV Recruitment</h2>
    <p>Neque porro quisquam est, qui dolorem ipsum quia dolor sit amet, consectetur, adipisci velit, rat voluptatem.</p>
    <span class="btn">READ MORE</span>
  </div>
</section>
<div class="abs arrow" style="left:58px"><svg width="8" height="12" viewBox="0 0 8 12"><path d="M6 1L1 6l5 5" stroke="#fff" stroke-width="2" fill="none"/></svg></div>
<div class="abs arrow" style="left:612px"><svg width="8" height="12" viewBox="0 0 8 12"><path d="M2 1l5 5-5 5" stroke="#fff" stroke-width="2" fill="none"/></svg></div>

<div class="abs cta">Expats looking for a job in Dubai? <span class="outline">Submit Your CV</span></div>

<h2 class="abs section-title" style="left:0;width:694px;text-align:center;top:478px">OUR SERVICES</h2>
<div class="abs rule" style="left:57px;top:513px;width:580px"><b style="width:60px;margin-left:260px"></b></div>

<div class="abs service" style="left:57px;top:555px"><div class="photo" role="img" aria-label="Group of smiling workers" style="background:linear-gradient(#cfd8e0,#6f8fae)"></div><div><h3>LABOR RECRUITMENT</h3><p>Nemo enim ipsam voluptatem quia voluptas sit aspernatur aut odit aut fugit, sed quia consequuntur magni dolores ...</p></div></div>
<div class="abs service" style="left:356px;top:555px"><div class="photo" role="img" aria-label="Business handshake at a meeting" style="background:linear-gradient(#e4e8ee,#7d8a9c)"></div><div><h3>SKILLED WORKERS</h3><p>Nemo enim ipsam voluptatem quia voluptas sit aspernatur aut odit aut fugit, sed quia consequuntur magni dolores ...</p></div></div>
<div class="abs service" style="left:57px;top:644px"><div class="photo" role="img" aria-label="Worker holding a yellow hard hat" style="background:linear-gradient(135deg,#e0b820,#3e4a55 55%)"></div><div><h3>UNSKILLED WORKERS</h3><p>Nemo enim ipsam voluptatem quia voluptas sit aspernatur aut odit aut fugit, sed quia consequuntur magni dolores ...</p></div></div>
<div class="abs service" style="left:356px;top:644px"><div class="photo" role="img" aria-label="Construction workers in hard hats" style="background:linear-gradient(#e8a040,#c2452e 60%,#8a6a40)"></div><div><h3>HOME HELPERS</h3><p>Nemo enim ipsam voluptatem quia voluptas sit aspernatur aut odit aut fugit, sed quia consequuntur magni dolores ...</p></div></div>

<section class="abs white-band">
  <h2 class="abs section-title" style="left:57px;top:28px">OUR PHILOSOPHY</h2>
  <div class="abs rule" style="left:57px;top:63px;width:283px"><b style="width:62px"></b></div>
  <div class="abs" role="img" aria-label="Hand touching a network of connected people icons" style="left:57px;top:88px;width:159px;height:125px;background:linear-gradient(120deg,#b8bcc2,#6e747c)"></div>
  <p class="abs" style="left:224px;top:86px;width:116px;font-size:6.8px;line-height:1.75">Nemo enim ipsam voluptatem quia voluptas sit aspernatur aut odit aut fugit, sed quia consequuntur magni dolores eos qui ratione voluptatem sequi nesciunt. Neque porro quisquam est, qui dolorem ipsum quia dolor sit amet, consectetur, adipisci velit, sed quia non numquam eius modi tempora incidunt ut labore et dolore magnam aliquam quaerat voluptatem.</p>

  <h2 class="abs section-title" style="left:355px;top:28px">TESTIMONIALS</h2>
  <div class="abs sq" style="left:581px;top:24px"><svg width="5" height="7" viewBox="0 0 5 7"><path d="M4 1L1 3.5 4 6" stroke="#555" fill="none"/></svg></div>
  <div class="abs sq" style="left:611px;top:24px"><svg width="5" height="7" viewBox="0 0 5 7"><path d="M1 1l3 2.5L1 6" stroke="#555" fill="none"/></svg></div>
  <div class="abs rule" style="left:355px;top:63px;width:282px"><b style="width:62px"></b></div>
  <div class="abs" role="img" aria-label="Portrait of a businesswoman" style="left:354px;top:90px;width:65px;height:64px;background:linear-gradient(#e6ece6,#6a6a6a)"></div>
  <div class="abs" style="left:430px;top:86px;width:207px;font-size:6.8px;line-height:1.75">
    <p>Nemo enim ipsam voluptatem quia voluptas sit aspernatur aut odit aut fugit.</p>
    <p style="margin-top:10px">sed quia consequuntur magni dolores eos qui ratione voluptatem sequi nesciunt. Neque porro quisquam est, qui dolorem ipsum quia dolor sit amet, consectetur, adipisci velit, sed quia non numquam eius modi tempora incidunt ut labore et dolore magnam aliquam quaerat voluptatem.</p>
    <p style="margin-top:10px;color:var(--ink);font-size:7.5px">- John Doe</p>
  </div>
</section>

<footer class="abs footer">
  <div class="abs" style="left:57px;top:24px;width:140px">
    <h4>ABOUT US</h4>
    <div class="brand" style="position:static;margin:6px 0 34px"><i></i>KTV</div>
    <p style="font-size:6.8px;line-height:1.75">Nemo enim ipsam voluptatem quia voluptas sit aspernatur aut odit aut fugit, sed quia consequuntur magni</p>
  </div>
  <div class="abs" style="left:238px;top:24px"><h4>QUICK LINKS</h4><ul><li>Home</li><li>About us</li><li>Philosophy</li><li>Services</li><li>Search CV</li><li>Testimonials</li><li>Contact us</li></ul></div>
  <div class="abs" style="left:360px;top:24px"><h4>SERVICES</h4><ul><li>Labor Recruitment</li><li>skilled workers</li><li>unskilled workers</li><li>Home Helpers</li></ul></div>
  <div class="abs" style="left:478px;top:24px;width:160px">
    <h4>CONTACT</h4>
    <div class="contact-item" style="font-size:6.8px;gap:12px"><svg width="8" height="8" viewBox="0 0 24 24"><path fill="#888" d="M12 3l10 9h-3v9h-5v-6h-4v6H5v-9H2z"/></svg><span>Nemo enim ipsam voluptatem quia voluptas sit aspernatur aut odit aut fugit.</span></div>
    <div class="contact-item" style="font-size:7px;gap:12px;margin-top:8px"><svg width="9" height="9" viewBox="0 0 24 24"><path fill="#888" d="M6.6 10.8a15 15 0 006.6 6.6l2.2-2.2a1 1 0 011-.25 11 11 0 003.6.6 1 1 0 011 1V20a1 1 0 01-1 1A17 17 0 013 4a1 1 0 011-1h3.5a1 1 0 011 1 11 11 0 00.6 3.6 1 1 0 01-.25 1z"/></svg><span>+ 100 2 555 0199</span></div>
    <div class="contact-item" style="font-size:7px;gap:12px;margin-top:14px"><svg width="9" height="8" viewBox="0 0 24 20"><rect x="1" y="1" width="22" height="18" fill="none" stroke="#888" stroke-width="2"/><path d="M1 2l11 9 11-9" fill="none" stroke="#888" stroke-width="2"/></svg><span>info@yourdomain.com</span></div>
  </div>
</footer>

<div class="abs bottom">© 2015 KTV recruitment. All rights reserved.</div>

</body>
</html>
```